Create a Business Card Design Project for a new logistics company

We need a business card designed for a new company in Australia.

Type of business is logistics/trucking.

Medium will be brushed black metal card that can/will be acid etched to a brushed steel silver, acid die cut and two printed colours of our choice which will be white and pantone orange.

We have hopes that the design will be simple, modern and represent with a quick glance what our company does.

Please read instructions carefully in must have box any questions please ask.

If you are interested in this job please look at other job that we have which is very similar with logo and design

Please have a look at the things that can be done with metals cards on google images for inspiration.

Target Market(s)

Men from 20yrs of age to 60yrs of age

Industry/Entity Type

Steel

Requirements
Must have
• Must Have:
- Front of card:

Must use the company logo and name provided as attachment (see below KVR-black-background-cmyk).
Logo grey will be etched, orange and white will be printed on card. Parts of the logo could even be die cut.

The word -Logistics anytime, anywhere- on front etched, printed or die cut.

detail needed on front or back depending on your design layout.

Name
position
email
mobile

all details can be on front if a nice design is etched on the back of card or to keep front simple you can put all detail on back of card, I will leave the lay out to you.

Colours in logo are

Pantone 144 C Orange
Pantone 11-0601 White
Pantone 7539 C Gray
Pantone 426 C Black

However black will be the base of black metal card. Gray will be replaced with the etching in card revealing the silver. Orange and white will be printed on card.

have fun!!
Nice to have
• The file attached called idea is just an example of what can be designed and etched into card. Google has many more idea's for metal business cards.
Should not have
• Please don't clutter the card
No fonts smaller then 7 points

```html
<!DOCTYPE html>
<html lang="en">
<head>
<meta charset="utf-8">
<title>KVR Business Card</title>
<link rel="stylesheet" href="https://fonts.googleapis.com/css2?family=Oswald:wght@500;700&family=Roboto+Condensed:wght@400;700&display=swap">
<style>
  :root {
    --backdrop: #2a2a2a;
    --card-black: #141414;
    --card-sheen: #262626;
    --orange: #f58a1f;
    --white: #f2f2f2;
    --steel: #b9bcbf;
    --steel-dark: #7d8084;
  }
  * { margin: 0; padding: 0; box-sizing: border-box; }
  html, body { width: 1200px; height: 809px; overflow: hidden; }
  body {
    background: var(--backdrop);
    font-family: "Roboto Condensed", sans-serif;
    color: var(--white);
    position: relative;
  }
  .card {
    position: absolute;
    width: 500px;
    height: 286px;
    border-radius: 6px;
    overflow: hidden;
    background: linear-gradient(115deg, var(--card-black) 0%, var(--card-sheen) 45%, var(--card-black) 100%);
    box-shadow: 0 18px 40px rgba(0,0,0,0.55);
  }
  .card--front { left: 80px; top: 130px; }
  .card--back { left: 620px; top: 330px; }

  .wordmark {
    position: absolute;
    display: flex;
    align-items: center;
    gap: 10px;
  }
  .wordmark__dot {
    width: 26px; height: 26px;
    border-radius: 50%;
    background: var(--steel);
  }
  .wordmark__name {
    font-family: "Oswald", sans-serif;
    font-weight: 700;
    font-size: 38px;
    line-height: 1;
    letter-spacing: 2px;
    color: var(--orange);
  }

  /* front */
  .card--front .wordmark { left: 34px; top: 72px; }
  .front__disc {
    position: absolute;
    right: -40px; top: -60px;
    width: 210px; height: 210px;
    border-radius: 50%;
    background: radial-gradient(circle at 40% 40%, #e6e7e8 0%, var(--steel) 45%, var(--steel-dark) 100%);
  }
  .front__band {
    position: absolute;
    left: 0; right: 0; top: 150px;
    height: 38px;
    background: var(--orange);
    display: flex;
    align-items: center;
    padding-left: 40px;
  }
  .front__tagline {
    font-size: 22px;
    letter-spacing: 1.5px;
    color: var(--card-black);
  }

  /* back */
  .card--back .wordmark { left: 40px; top: 92px; }
  .back__rule {
    position: absolute;
    left: 90px; right: 20px; top: 150px;
    height: 1px;
    background: linear-gradient(90deg, rgba(255,255,255,0) 0%, var(--steel) 25%, var(--steel) 80%, rgba(255,255,255,0) 100%);
  }
  .back__person {
    position: absolute;
    right: 34px; top: 52px;
    text-align: right;
  }
  .back__name {
    font-family: "Oswald", sans-serif;
    font-weight: 500;
    font-size: 24px;
    letter-spacing: 1px;
    color: var(--orange);
    text-transform: uppercase;
  }
  .back__role {
    font-size: 14px;
    font-weight: 700;
    color: var(--white);
  }
  .back__contacts {
    position: absolute;
    left: 150px; top: 180px;
    list-style: none;
  }
  .back__contacts li {
    display: flex;
    align-items: center;
    gap: 12px;
    font-size: 19px;
    letter-spacing: 0.5px;
    margin-bottom: 12px;
  }
  .back__contacts svg { width: 16px; height: 16px; fill: var(--orange); }

  .presentation-mark { right: 90px; bottom: 48px; }
  .presentation-mark .wordmark__name { font-size: 34px; }
</style>
</head>
<body>

  <section class="card card--front" aria-label="Card front">
    <div class="front__disc" aria-hidden="true"></div>
    <div class="wordmark">
      <span class="wordmark__dot"></span>
      <span class="wordmark__name">KVR</span>
    </div>
    <div class="front__band">
      <p class="front__tagline">Logistics anytime, anywhere</p>
    </div>
  </section>

  <section class="card card--back" aria-label="Card back">
    <div class="wordmark">
      <span class="wordmark__dot"></span>
      <span class="wordmark__name">KVR</span>
    </div>
    <div class="back__person">
      <p class="back__name">Liam Carter</p>
      <p class="back__role">Managing Director</p>
    </div>
    <div class="back__rule"></div>
    <ul class="back__contacts">
      <li>
        <svg viewBox="0 0 16 16" aria-hidden="true"><rect x="4" y="1" width="8" height="14" rx="1.5"/><rect x="5.5" y="3" width="5" height="7" fill="#141414"/></svg>
        <span>0400 123 987</span>
      </li>
      <li>
        <svg viewBox="0 0 16 16" aria-hidden="true"><rect x="1" y="3" width="14" height="10" rx="1"/><path d="M1.5 3.5 8 9l6.5-5.5" stroke="#141414" stroke-width="1.4" fill="none"/></svg>
        <span>liamcarter@kvr.com.au</span>
      </li>
    </ul>
  </section>

  <div class="wordmark presentation-mark">
    <span class="wordmark__dot"></span>
    <span class="wordmark__name">KVR</span>
  </div>

</body>
</html>
```